TLW Facebook Page Cover Image

I am setting up a Facebook company page for my new business called 'TidewaterLinkWorks'. We provide business owners, executives, and managers with valuable information via a comprehensive suite of employee assessment products to make better people decisions. Company tagline is Staff Smarter - Grow Teams - Reach Targets. I need a attention grabbing, polished, professional cover graphic to be displayed on the top of the page that captures who we are and is a nice compliment to our logo which will appear in the smaller logo box. Company personality is contemporary, energetic, competent yet humble. Logo is attached. Please view our 3 minute overview video on YouTube to get a sense of who we are/what we do. https://www.examplevideohost.net/watch?v=Qor7mTa2LpW

Target Market(s)

My website is a B2B website. My ideal "sweet spot" client company employees approximately 200-300 employees, although my secondary products and service market will include companies above 200-300 employees to include select Fortune 500 companies. Target client roles within these companies include:
- Business Leaders - CEO's, Presidents, and General Managers
- Small & Mid-sized business owners
- Functional Leaders - CFOs, CIO, Sales/Marketing leaders, HR leaders
- Functional Specialists - Recruiting, Learning & Development, OD
- 1st and 2nd line managers
Our products and services can be used effectively across all industries, but if I had to pick the top 5 or 6 "target" industries or type of businesses that match extremely well to our products/services I'd say retail/consumer products, healthcare/human services, direct/outside sales (*e.g. car dealers, medical equipment sales, telemarketing, etc.), customer service call centers, hospitality, and banking.

Industry/Entity Type

Business

Font styles to use
Sans Serif

Requirements
Nice to have
• Don't want the graphic to be too busy or crowded. Photography and/or from scratch graphics can be used separately or in combination. Attached is a sample from an unrelated web page I like in terms of it's white space/graphic/text balance.

```html
<!DOCTYPE html>
<html lang="en">
<head>
<meta charset="utf-8">
<title>TidewaterLinkWorks – Cover</title>
<link href="https://fonts.googleapis.com/css2?family=Archivo+Black&family=Montserrat:wght@400;700&display=swap" rel="stylesheet">
<style>
  :root {
    --sky-light: #7ccdf3;
    --sky-right: #7eafd6;
    --sky-text: #3ea5e6;
    --ground: #1ba3e4;
    --ground-deep: #0f93d6;
    --stripe: #ffe01a;
    --figure: #1c1f2b;
    --brand-navy: #2b2f7d;
    --brand-soft: #3d62a6;
    --mark: #2e6fc0;
  }
  html, body {
    margin: 0;
    padding: 0;
    overflow: hidden;
    background: #ffffff;
  }
  .cover {
    position: relative;
    width: 1200px;
    height: 444px;
    overflow: hidden;
    background: linear-gradient(90deg, var(--sky-light) 0%, #73c2ee 60%, var(--sky-right) 100%);
  }
  .ground {
    position: absolute;
    left: 0;
    top: 303px;
    width: 1200px;
    height: 141px;
    background: linear-gradient(180deg, var(--ground) 0%, var(--ground-deep) 100%);
  }
  .headline {
    position: absolute;
    left: -6px;
    top: -22px;
    margin: 0;
    font-family: "Archivo Black", "Arial Black", sans-serif;
    font-size: 118px;
    line-height: 99px;
    letter-spacing: 3px;
    color: var(--sky-text);
    text-transform: uppercase;
    white-space: nowrap;
  }
  .headline span { display: block; }
  .stripes {
    position: absolute;
    left: 0;
    top: 0;
  }
  .stripe {
    fill: none;
    stroke: var(--stripe);
    stroke-width: 14;
    stroke-linejoin: miter;
    stroke-miterlimit: 10;
  }
  .figure {
    position: absolute;
    background: var(--figure);
    border-radius: 14px 14px 4px 4px;
  }
  .figure--handshake { left: 113px; top: 176px; width: 92px; height: 127px; }
  .figure--cheer     { left: 282px; top: 218px; width: 63px; height: 118px; }
  .figure--walker    { left: 402px; top: 254px; width: 42px; height: 116px; }
  .brand {
    position: absolute;
    left: 905px;
    top: 250px;
    width: 260px;
    text-align: center;
    font-family: "Montserrat", Arial, sans-serif;
  }
  .brand__mark {
    display: block;
    width: 84px;
    height: 84px;
    margin: 0 auto 10px;
    border-radius: 50%;
    background: var(--mark);
  }
  .brand__name {
    display: block;
    font-weight: 700;
    font-size: 23px;
    color: var(--brand-navy);
    letter-spacing: -0.3px;
  }
  .brand__tagline {
    display: block;
    margin-top: 6px;
    padding-top: 5px;
    border-top: 1px solid var(--brand-soft);
    font-weight: 400;
    font-size: 11.5px;
    color: var(--brand-soft);
  }
</style>
</head>
<body>
  <main class="cover">
    <div class="ground"></div>

    <h1 class="headline">
      <span>Staff Smarter</span>
      <span>Grow Teams</span>
      <span>Reach Targets</span>
    </h1>

    <svg class="stripes" width="1200" height="444" viewBox="0 0 1200 444" aria-hidden="true">
      <defs>
        <path id="growth-line" d="M40 303 H262 L412 450 L690 150 L770 270 L1120 -30"/>
      </defs>
      <use href="#growth-line" class="stripe"/>
      <use href="#growth-line" class="stripe" transform="translate(24 28)"/>
      <use href="#growth-line" class="stripe" transform="translate(48 56)"/>
    </svg>

    <div class="figure figure--handshake" role="img" aria-label="Two business people shaking hands"></div>
    <div class="figure figure--cheer" role="img" aria-label="Businessman with arms raised in celebration"></div>
    <div class="figure figure--walker" role="img" aria-label="Businesswoman walking up the path with a bag"></div>

    <div class="brand">
      <span class="brand__mark"></span>
      <span class="brand__name">TidewaterLinkWorks</span>
      <span class="brand__tagline">Staff Smarter • Grow Teams • Reach Targets</span>
    </div>
  </main>
</body>
</html>
```